Banner Pop Up Opt In Form REDESIGNS - SLEEK BLACK LOOK

Please redesign banners attached.

I am looking for a very sleek look....I do not like this collage of images on these current designs. Please keep all content same but use images that pop.

I have an acccount at www.pixmorrow-example.com or you can use your own images.

I like black background for somereason because it looks very sleek....but these designs should pop , build trust and credibility and have easy opt in form....SLEEK AND MODERN LOOK is what im looking for....

Target Market(s)

Consumers on websites

Requirements
Must have
• Please redesign banners attached.

Nice to have

Should not have

```html
<!DOCTYPE html>
<html lang="en">
<head>
<meta charset="utf-8">
<title>Newsletter Offer Banner</title>
<link rel="stylesheet" href="https://fonts.googleapis.com/css2?family=Open+Sans:wght@300;400;600;700&display=swap">
<style>
  :root {
    --panel-bg: #f6f6f6;
    --ink: #111111;
    --ink-soft: #444444;
    --field-bg: #a0a0a0;
    --field-text: #ffffff;
    --button-bg: #000000;
    --button-text: #ffffff;
    --note-text: #d2d6d6;
    --jungle-light: #7d9a52;
    --jungle-mid: #4c6a2c;
    --jungle-dark: #2c3f1c;
    --sea-light: #5fc2bb;
    --sea-mid: #2f9c97;
    --sea-dark: #0f2a2b;
  }
  * { margin: 0; padding: 0; box-sizing: border-box; }
  html, body {
    width: 1200px;
    height: 1032px;
    overflow: hidden;
    background: #ffffff;
  }
  .banner {
    position: relative;
    width: 1200px;
    height: 1032px;
    font-family: "Open Sans", Arial, sans-serif;
    overflow: hidden;
  }
  .hero-photo {
    position: absolute;
    left: 0; top: 0;
    width: 1200px;
    height: 284px;
    background:
      linear-gradient(180deg, var(--jungle-light) 0%, var(--jungle-mid) 55%, var(--jungle-dark) 100%);
  }
  .offer-panel {
    position: absolute;
    left: 0; top: 284px;
    width: 1200px;
    height: 443px;
    background: var(--panel-bg);
    text-align: center;
  }
  .offer-title {
    position: absolute;
    left: 0; right: 0; top: 34px;
    font-size: 67px;
    font-weight: 600;
    line-height: 1;
    color: var(--ink);
    letter-spacing: 0.5px;
  }
  .offer-subtitle {
    position: absolute;
    left: 0; right: 0; top: 112px;
    font-size: 21px;
    font-weight: 600;
    line-height: 1;
    color: var(--ink-soft);
    letter-spacing: 0.4px;
  }
  .offer-prize {
    position: absolute;
    left: 0; right: 0; top: 152px;
    font-size: 37px;
    font-weight: 400;
    line-height: 1;
    color: var(--ink-soft);
    letter-spacing: 0.6px;
  }
  .offer-prize strong { font-weight: 700; }
  .optin-form {
    position: absolute;
    left: 16px; top: 237px;
    width: 1163px;
    display: grid;
    grid-template-columns: 578px 577px;
    grid-template-rows: 84px 84px;
    column-gap: 8px;
    row-gap: 8px;
  }
  .optin-field {
    border: none;
    background: var(--field-bg);
    color: var(--field-text);
    font-family: "Open Sans", Arial, sans-serif;
    font-size: 31px;
    font-weight: 300;
    padding: 0 36px;
    outline: none;
  }
  .optin-field::placeholder { color: var(--field-text); opacity: 1; }
  .optin-submit {
    border: none;
    background: var(--button-bg);
    color: var(--button-text);
    font-family: "Open Sans", Arial, sans-serif;
    font-size: 30px;
    font-weight: 700;
    text-align: left;
    padding: 0 36px;
    cursor: pointer;
    letter-spacing: 0.5px;
  }
  .sea-photo {
    position: absolute;
    left: 0; top: 727px;
    width: 1200px;
    height: 305px;
    background:
      linear-gradient(180deg, var(--sea-light) 0%, var(--sea-mid) 45%, var(--sea-dark) 100%);
  }
  .redeem-note {
    position: absolute;
    left: 0; right: 0; top: 980px;
    text-align: center;
    font-size: 22px;
    font-weight: 400;
    color: var(--note-text);
  }
</style>
</head>
<body>
  <main class="banner">
    <div class="hero-photo" role="img" aria-label="Lush green rice terraces with palm trees"></div>

    <section class="offer-panel">
      <h1 class="offer-title">WANT A GREAT OFFER?</h1>
      <p class="offer-subtitle">SUBSCRIBE TO OUR NEWSLETTER AND RECEIVE A COMPLIMENTARY</p>
      <p class="offer-prize"><strong>$300</strong> RESTAURANT CERTIFICATE</p>

      <form class="optin-form">
        <input class="optin-field" type="text" name="name" placeholder="Name">
        <input class="optin-field" type="tel" name="phone" placeholder="Phone">
        <input class="optin-field" type="email" name="email" placeholder="Email">
        <button class="optin-submit" type="submit">SUBMIT</button>
      </form>
    </section>

    <div class="sea-photo" role="img" aria-label="Aerial view of a paddleboarder on clear turquoise water"></div>
    <p class="redeem-note">We will send an email and text message with the offer and instructions on how to redeem.</p>
  </main>
</body>
</html>
```